Tiny Sprout nursery
Learning throu fun & activities
Bright & Fun-filled
Rashid Al Fahim (K-07)
tinysprout_ns@quellmail.com
www.tinysprout-ns.com
P.O.Box 51862
To be as points
Logo vector file

```html
<!DOCTYPE html>
<html lang="en">
<head>
<meta charset="utf-8">
<title>Tiny Sprout nursery – Business Card</title>
<link href="https://fonts.googleapis.com/css2?family=Arimo:wght@400;700&display=swap" rel="stylesheet">
<style>
  :root {
    --stage: #151515;
    --card-orange: #f6a21c;
    --card-orange-deep: #ec8f12;
    --ink: #3a230c;
    --ink-soft: #5a3812;
    --art-skin: #f3d3a5;
    --art-skin-light: #f8e2c0;
    --art-pink: #d9317f;
    --art-outline: #2b1a0a;
    --silhouette: #e08a10;
  }
  * { box-sizing: border-box; margin: 0; padding: 0; }
  html, body {
    width: 1200px; height: 871px; overflow: hidden;
    background: var(--stage);
  }
  .stage {
    width: 1200px; height: 871px;
    display: flex; align-items: center; justify-content: center; gap: 40px;
  }
  .card {
    position: relative;
    width: 540px; height: 310px;
    border-radius: 26px;
    background: linear-gradient(160deg, var(--card-orange) 0%, var(--card-orange-deep) 100%);
    overflow: hidden;
    font-family: "Arimo", Arial, sans-serif;
    color: var(--ink);
  }
  /* Front: contact details */
  .contact {
    position: absolute; left: 32px; top: 36px;
    width: 256px;
    font-size: 13px; line-height: 1.45;
  }
  .contact .name { font-weight: 700; font-size: 15px; margin-bottom: 4px; color: var(--ink); }
  .contact p { color: var(--ink-soft); white-space: nowrap; }
  .mascot-art {
    position: absolute; right: 22px; top: 20px;
    width: 218px; height: 270px;
  }
  /* Back: logo and tagline */
  .silhouette-art {
    position: absolute; left: -30px; top: 30px;
    width: 250px; height: 300px;
  }
  .brand {
    position: absolute; right: 40px; top: 70px;
    display: flex; align-items: center; gap: 14px;
  }
  .brand-dot {
    width: 34px; height: 34px; border-radius: 50%;
    background: var(--art-pink);
    flex: none;
  }
  .brand-name {
    font-weight: 700; font-size: 30px; line-height: 1.05;
    color: var(--ink); width: 200px;
  }
  .tagline {
    position: absolute; right: 40px; top: 160px; width: 254px;
    font-weight: 700; font-size: 15px; color: var(--ink);
  }
</style>
</head>
<body>
<main class="stage">
  <section class="card card-front" aria-label="Business card front">
    <div class="contact">
      <p class="name">Rashid Al Fahim (K-07)</p>
      <p>Phone : 02-4471236</p>
      <p>Cell : 050-218-7753</p>
      <p>Fax : 02-4471239</p>
      <p>Email : tinysprout_ns@quellmail.com</p>
      <p>www.tinysprout-ns.com</p>
      <p>P.O.Box 51862</p>
    </div>
    <svg class="mascot-art" viewBox="0 0 218 270" role="img" aria-label="Cartoon baby mascot in a pink top and white nappy, waving">
      <defs>
        <linearGradient id="mascotFill" x1="0" y1="0" x2="0" y2="1">
          <stop offset="0" stop-color="var(--art-skin-light)"/>
          <stop offset="0.45" stop-color="var(--art-skin)"/>
          <stop offset="0.8" stop-color="var(--art-pink)" stop-opacity="0.85"/>
          <stop offset="1" stop-color="var(--art-skin-light)"/>
        </linearGradient>
      </defs>
      <rect x="4" y="4" width="210" height="262" rx="70" fill="url(#mascotFill)" stroke="var(--art-outline)" stroke-width="5"/>
    </svg>
  </section>

  <section class="card card-back" aria-label="Business card back">
    <svg class="silhouette-art" viewBox="0 0 250 300" role="img" aria-label="Faint silhouette of the baby mascot as background decoration">
      <rect x="0" y="0" width="250" height="300" rx="110" fill="var(--silhouette)" opacity="0.55"/>
    </svg>
    <div class="brand">
      <span class="brand-dot"></span>
      <span class="brand-name">Tiny Sprout nursery</span>
    </div>
    <p class="tagline">Learning through Fun &amp; Activities</p>
  </section>
</main>
</body>
</html>
```